broucher for electrical contracting buisness

use website template and attached files for colour scheme / ideas

Industry/Entity Type

Electrical

Requirements
Must have
• A5 folded to A4 4 pp format
• use the written content in the broucher word document as a guide

```html
<!DOCTYPE html>
<html lang="en">
<head>
<meta charset="utf-8">
<title>Calder Electrical – Brochure</title>
<link href="https://fonts.googleapis.com/css2?family=Montserrat:wght@600;700;800&family=Open+Sans:wght@400;600&display=swap" rel="stylesheet">
<style>
:root{
  --blue:#1c4e9d;
  --blue-dark:#123a78;
  --red:#d7262c;
  --ink:#333a44;
  --grey:#6b7380;
  --paper:#ffffff;
  --light:#f1f3f6;
  --stage:#e6e8ec;
}
*{box-sizing:border-box;margin:0;padding:0}
html,body{width:880px;height:1200px;overflow:hidden}
body{background:var(--stage);font-family:"Open Sans",Arial,sans-serif;color:var(--ink);position:relative}
.spread{position:absolute;left:50px;width:780px;height:552px;display:flex;background:var(--paper);box-shadow:0 6px 18px rgba(0,0,0,.18)}
.spread--outer{top:32px}
.spread--inner{top:616px}
.page{position:relative;width:390px;height:552px;overflow:hidden}
.page + .page{border-left:1px solid #e2e5ea}
.copy{font-size:6.6px;line-height:1.5;color:var(--grey)}
.photo{position:absolute}
.brand{display:flex;align-items:center;gap:6px;font-family:"Montserrat",sans-serif;font-weight:800;color:var(--blue);letter-spacing:.5px}
.brand__mark{background:var(--red)}
.heading{font-family:"Montserrat",sans-serif;font-weight:700;text-transform:uppercase;letter-spacing:.4px}

/* back cover */
.back__intro{position:absolute;left:28px;top:30px;width:320px}
.back__intro p+p{margin-top:6px}
.back__photo{left:28px;top:104px;width:334px;height:168px;background:linear-gradient(160deg,#f4f4f2 0%,#d9dde2 55%,#b8bec7 100%)}
.contact{position:absolute;left:28px;top:296px;width:220px}
.contact .heading{color:var(--red);font-size:10px;margin-bottom:8px}
.contact li{list-style:none;display:flex;align-items:center;gap:7px;font-size:7px;color:var(--ink);margin-bottom:6px}
.contact svg{width:10px;height:10px;flex:none}
.back__brand{position:absolute;left:210px;top:410px;font-size:15px}
.back__brand .brand__mark{width:12px;height:12px}
.back__stripes{position:absolute;left:0;bottom:0;width:390px;height:70px}
.back__web{position:absolute;left:30px;bottom:12px;font-size:7.5px;color:#fff;font-weight:600}

/* front cover */
.front__brand{position:absolute;left:0;right:0;top:22px;justify-content:center;font-size:20px}
.front__brand .brand__mark{width:16px;height:16px}
.front__photo{left:0;top:64px;width:390px;height:262px;background:linear-gradient(135deg,#3a4654 0%,#c9ccd0 40%,#e7a23a 62%,#5d6672 100%)}
.front__panel{position:absolute;left:0;top:326px;width:390px;height:226px}
.front__claim{position:absolute;left:150px;top:352px;width:220px;font-family:"Montserrat",sans-serif}
.front__claim .big{color:var(--red);font-weight:800;font-size:17px;line-height:1}
.front__claim .mid{color:var(--blue);font-weight:700;font-size:8.5px;margin-top:4px;text-transform:uppercase}
.front__claim .small{color:var(--red);font-weight:600;font-size:7px;margin-top:3px;text-transform:uppercase}
.badge247{position:absolute;width:64px;height:64px;border-radius:50%;background:var(--paper);border:3px solid var(--red);display:flex;flex-direction:column;align-items:center;justify-content:center;font-family:"Montserrat",sans-serif}
.badge247 b{color:var(--blue);font-size:17px;font-weight:800;line-height:1}
.badge247 span{color:var(--red);font-size:6px;font-weight:700;text-transform:uppercase}
.front .badge247{right:18px;top:410px}
.callbar{position:absolute;display:flex;height:24px;font-family:"Montserrat",sans-serif;font-weight:700;font-size:8px;color:#fff;align-items:stretch}
.callbar__label{background:var(--blue);padding:0 10px;display:flex;align-items:center}
.callbar__num{background:var(--red);padding:0 12px;display:flex;align-items:center}
.front .callbar{right:0;bottom:26px}

/* inner pages */
.inner{padding:24px 26px}
.inner .heading{font-size:8px;color:var(--blue);margin:10px 0 3px}
.inner .heading.title{font-size:12px;color:var(--red);margin-top:0}
.tiles{display:flex;gap:8px;margin:10px 0 4px}
.tile{flex:1;text-align:center;font-size:6.5px;font-weight:600;color:var(--blue)}
.tile__img{height:38px;border-radius:3px;margin-bottom:3px;background:linear-gradient(135deg,#5a6b80,#c8d0da)}
.row{display:flex;gap:12px;align-items:flex-start}
.row .copy{flex:1}
.smoke-photo{position:static;width:78px;height:60px;border-radius:50%;background:radial-gradient(circle,#ffffff 30%,#dfe3e8 75%,#c3c9d1 100%);flex:none;margin-top:6px}
.breaker-photo{position:static;width:78px;height:88px;background:linear-gradient(180deg,#f3f4f6,#cfd4db);flex:none;margin-top:6px}
.ac-photo{position:static;width:130px;height:44px;border-radius:4px;background:linear-gradient(180deg,#fbfbfb,#d8dce2);flex:none;margin-top:6px}
.inner-left__foot{position:absolute;left:0;bottom:0;width:390px;height:46px;background:var(--light);display:flex;align-items:center;gap:12px;padding:0 26px}
.cert{width:26px;height:26px;border-radius:50%;background:#c9ced6}
.cert.square{border-radius:3px;background:#b7bec8}
.inner-right .badge247{left:26px;bottom:50px;width:54px;height:54px}
.inner-right .badge247 b{font-size:14px}
.inner-right .callbar{right:0;bottom:64px}
.inner-right__foot{position:absolute;left:0;bottom:0;width:390px;height:34px;background:var(--blue);display:flex;align-items:center;justify-content:space-between;padding:0 26px;color:#fff;font-size:7px;font-weight:600}
.inner-right__foot .accent{position:absolute;right:0;top:0;width:120px;height:34px;background:var(--red);clip-path:polygon(16% 0,100% 0,100% 100%,0 100%)}
.inner-right__foot span{position:relative}
</style>
</head>
<body>

<section class="spread spread--outer">
  <article class="page back">
    <div class="back__intro copy">
      <p>Calder Electrical is a family owned contractor serving homes, shops and offices across the region for over fifteen years. Our licensed team delivers safe, tidy and reliable work on every job.</p>
      <p>We quote clearly, arrive on time and leave every site clean. From a single power point to a full fit-out, you can count on us.</p>
    </div>
    <div class="photo back__photo" role="img" aria-label="Bright modern interior with recessed ceiling lighting"></div>
    <div class="contact">
      <h3 class="heading">Contact Details</h3>
      <ul>
        <li><svg viewBox="0 0 10 10"><circle cx="5" cy="5" r="5" fill="#d7262c"/><path d="M3.3 2.6l1 .9-.5.8a4 4 0 0 0 1.9 1.9l.8-.5.9 1-.7.8C4.9 7.3 2.7 5.1 2.5 3.3z" fill="#fff"/></svg>1300 555 014 &nbsp;|&nbsp; 0400 555 278</li>
        <li><svg viewBox="0 0 10 10"><circle cx="5" cy="5" r="5" fill="#d7262c"/><rect x="2.4" y="3.2" width="5.2" height="3.6" fill="#fff"/><path d="M2.4 3.2L5 5.2l2.6-2" stroke="#d7262c" stroke-width=".6" fill="none"/></svg>info@calderelectrical.net</li>
        <li><svg viewBox="0 0 10 10"><circle cx="5" cy="5" r="5" fill="#d7262c"/><path d="M5 2.2a1.8 1.8 0 0 1 1.8 1.8C6.8 5.4 5 7.8 5 7.8S3.2 5.4 3.2 4A1.8 1.8 0 0 1 5 2.2z" fill="#fff"/></svg>18 Foundry Lane, Northgate</li>
        <li><svg viewBox="0 0 10 10"><circle cx="5" cy="5" r="5" fill="#d7262c"/><circle cx="5" cy="5" r="2.6" fill="none" stroke="#fff" stroke-width=".7"/><path d="M2.4 5h5.2M5 2.4v5.2" stroke="#fff" stroke-width=".6"/></svg>www.calderelectrical.net</li>
      </ul>
    </div>
    <div class="brand back__brand"><span class="brand__mark"></span>CALDER ELECTRICAL</div>
    <svg class="back__stripes" viewBox="0 0 390 70" preserveAspectRatio="none">
      <polygon points="0,22 390,48 390,70 0,70" fill="#1c4e9d"/>
      <polygon points="0,30 260,52 260,70 0,70" fill="#d7262c"/>
    </svg>
    <div class="back__web">www.calderelectrical.net</div>
  </article>

  <article class="page front">
    <div class="brand front__brand"><span class="brand__mark"></span>CALDER ELECTRICAL</div>
    <div class="photo front__photo" role="img" aria-label="Electrician testing a switchboard with a multimeter"></div>
    <svg class="front__panel" viewBox="0 0 390 226" preserveAspectRatio="none">
      <polygon points="0,0 130,0 100,226 0,226" fill="#1c4e9d"/>
      <polygon points="118,0 132,0 102,226 88,226" fill="#d7262c"/>
    </svg>
    <div class="front__claim">
      <div class="big">WE PRIDE</div>
      <div class="mid">Ourselves on quality workmanship</div>
      <div class="small">By licensed electricians you can trust</div>
    </div>
    <div class="badge247"><b>24/7</b><span>Emergency</span></div>
    <div class="callbar"><span class="callbar__label">CALL US NOW</span><span class="callbar__num">1300 555 014</span></div>
  </article>
</section>

<section class="spread spread--inner">
  <article class="page inner inner-left">
    <h2 class="heading title">Our Services</h2>
    <p class="copy">We offer a complete range of electrical services for residential, commercial and industrial clients, all backed by our workmanship guarantee.</p>
    <div class="tiles">
      <div class="tile"><div class="tile__img" role="img" aria-label="Lighting installation"></div>Lighting</div>
      <div class="tile"><div class="tile__img" role="img" aria-label="Power outlets"></div>Power</div>
      <div class="tile"><div class="tile__img" role="img" aria-label="Safety testing"></div>Safety</div>
      <div class="tile"><div class="tile__img" role="img" aria-label="Data cabling"></div>Data</div>
    </div>
    <h3 class="heading">Electrical Installations</h3>
    <p class="copy">New builds, renovations and extensions wired to current standards, with neat cabling, quality fittings and full compliance certificates on completion.</p>
    <div class="row">
      <div class="copy">
        <h3 class="heading">Smoke Alarms</h3>
        <p>Supply, installation and testing of photoelectric smoke alarms, hard-wired and interconnected to keep your family and tenants protected.</p>
      </div>
      <div class="photo smoke-photo" role="img" aria-label="Ceiling smoke alarm"></div>
    </div>
    <div class="row">
      <div class="photo breaker-photo" role="img" aria-label="Circuit breaker in a switchboard"></div>
      <div class="copy">
        <h3 class="heading">Switchboard Upgrades</h3>
        <p>Replace old fuses with modern circuit breakers and safety switches to reduce fire risk and protect every circuit in the building.</p>
      </div>
    </div>
    <div class="inner-left__foot">
      <span class="cert"></span><span class="cert square"></span><span class="cert"></span><span class="cert square"></span><span class="cert"></span>
    </div>
  </article>

  <article class="page inner inner-right">
    <h3 class="heading">Commercial Services</h3>
    <p class="copy">Fit-outs, emergency and exit lighting, test and tag, and scheduled maintenance for offices, retail and warehouses, planned around your trading hours.</p>
    <h3 class="heading">Data &amp; Communications</h3>
    <p class="copy">Structured cabling, TV points, phone lines and network racks installed and labelled for fast, dependable connections.</p>
    <div class="row">
      <div class="copy">
        <h3 class="heading">Air Conditioning</h3>
        <p>Split system supply and installation, dedicated circuits and regular servicing so your home stays comfortable all year round.</p>
      </div>
      <div class="photo ac-photo" role="img" aria-label="Wall-mounted split system air conditioner"></div>
    </div>
    <h3 class="heading">Maintenance &amp; Repairs</h3>
    <p class="copy">Fault finding, rewiring and repairs completed promptly by friendly technicians who explain the work before they start.</p>
    <div class="badge247"><b>24/7</b><span>Emergency</span></div>
    <div class="callbar"><span class="callbar__label">CALL US NOW</span><span class="callbar__num">1300 555 014</span></div>
    <div class="inner-right__foot">
      <span>www.calderelectrical.net</span>
      <div class="accent"></div>
      <span>0400 555 278</span>
    </div>
  </article>
</section>

</body>
</html>
```